Business card

creative business card for newly created national firm that specializes in high-density storage for retail markets. Looking for creativity and overall theme that will differentiate from others in this unique niche ...essentially a design that will provide instant recognition as we develop our identity in the marketplace. possible initial thoughts are attached with logo separately

Industry/Entity Type

Retail

```html
<!DOCTYPE html>
<html lang="en">
<head>
<meta charset="utf-8">
<title>Shelfwise Storage Group – Business Card</title>
<link rel="stylesheet" href="https://fonts.googleapis.com/css2?family=Josefin+Sans:wght@300&family=Lato:wght@400;700&display=swap">
<style>
  :root {
    --page-bg: #ecebe8;
    --card-white: #f7f7f7;
    --card-edge: #dcdcdc;
    --band-blue: #45b3d8;
    --brand-teal: #2f7f9f;
    --text-blue: #3ab0dc;
    --text-white: #ffffff;
    --mark-blue: #5cc3e6;
  }
  * { box-sizing: border-box; margin: 0; padding: 0; }
  html, body {
    width: 1200px;
    height: 1023px;
    overflow: hidden;
    background: var(--page-bg);
  }
  .sheet {
    width: 1200px;
    height: 1023px;
    display: flex;
    flex-direction: column;
    align-items: center;
    justify-content: center;
    gap: 70px;
  }
  .card {
    width: 600px;
    height: 343px;
    border-radius: 22px;
    background: var(--card-white);
    border: 1px solid var(--card-edge);
    box-shadow: 0 10px 28px rgba(0,0,0,0.12);
    overflow: hidden;
    position: relative;
  }

  /* Front */
  .card-front {
    display: flex;
    align-items: center;
    padding-left: 70px;
  }
  .brand {
    display: flex;
    align-items: center;
    gap: 26px;
  }
  .brand-square {
    width: 58px;
    height: 58px;
    background: var(--mark-blue);
    flex: none;
  }
  .brand-name {
    font-family: "Josefin Sans", sans-serif;
    font-weight: 300;
    font-size: 50px;
    line-height: 0.98;
    letter-spacing: 1px;
    color: var(--brand-teal);
    text-transform: uppercase;
  }
  .tagline {
    position: absolute;
    left: 154px;
    bottom: 56px;
    font-family: "Lato", sans-serif;
    font-weight: 700;
    font-size: 17px;
    letter-spacing: 4px;
    color: var(--brand-teal);
  }

  /* Back */
  .card-back {
    display: flex;
    flex-direction: column;
  }
  .band-top {
    height: 62px;
    background: var(--band-blue);
  }
  .contact {
    flex: 1;
    padding: 30px 56px 0;
    font-family: "Lato", sans-serif;
    font-style: normal;
    font-weight: 400;
    font-size: 20px;
    line-height: 1.45;
    color: var(--text-blue);
  }
  .band-bottom {
    height: 72px;
    background: var(--band-blue);
    display: flex;
    align-items: center;
    padding-left: 56px;
  }
  .website {
    font-family: "Lato", sans-serif;
    font-weight: 700;
    font-size: 20px;
    color: var(--text-white);
    letter-spacing: 0.5px;
  }
</style>
</head>
<body>
  <main class="sheet">
    <section class="card card-front" aria-label="Card front">
      <div class="brand">
        <div class="brand-square"></div>
        <h1 class="brand-name">Shelfwise<br>Storage<br>Group</h1>
      </div>
      <p class="tagline">Rethink Every Shelf</p>
    </section>

    <section class="card card-back" aria-label="Card back">
      <div class="band-top"></div>
      <address class="contact">
        Phone Number<br>
        Street Address<br>
        Cedar Ridge, AZ 99999<br>
        info@shelfwisegroup.com
      </address>
      <div class="band-bottom">
        <span class="website">www.shelfwisegroup.com</span>
      </div>
    </section>
  </main>
</body>
</html>
```